This book will apply the 12 Steps to gaming addiction, also known as video game addiction. The primary purpose of the book is to provide an effective solution for this new type of addiction. The solution is based on the rich and successful concepts of traditional twelve-step programs like RW.

The title on the cover will be "The Nine Paths Past Screen Compulsion" and "by Orrin Falkett". A subtitle can be used if it works in your design of "A Practical Route Through Console Overuse". Cover will be for a 6" x 9" book approximately 110 pages in length.

Some back cover text including some review quotes and an author bio are in the attached Word doc. There is also an author photo attached for for the back cover.

Requirements
Must have
• For the cover design it could be stylized, or an image, a partial image, or whatever. I am open to suggestions. Think about what would be noticed by a person searching for help with moderating their video game use, or by the parents or loved ones of problem gamers. Something contemporary and eye catching.

```html
<!DOCTYPE html>
<html lang="en">
<head>
<meta charset="utf-8">
<title>The Nine Paths Past Screen Compulsion — Cover</title>
<link rel="stylesheet" href="https://fonts.googleapis.com/css2?family=Silkscreen:wght@400;700&family=PT+Sans:wght@400;700&display=swap">
<style>
  :root {
    --night: #04060d;
    --deep-blue: #0c1238;
    --glow-violet: #2f2a8c;
    --screen-cyan: #46c2e0;
    --screen-teal: #1d86ad;
    --screen-lime: #b8d24a;
    --screen-pink: #c04a8a;
    --title-white: #e4e6f4;
    --title-yellow: #d9df33;
    --title-yellow-dark: #a7ad1c;
    --title-red: #e8182c;
    --title-red-dark: #a80f1d;
    --subtitle: #d2d6ec;
  }
  * { margin: 0; padding: 0; box-sizing: border-box; }
  html, body { width: 800px; height: 1200px; overflow: hidden; background: var(--night); }
  .cover {
    position: relative;
    width: 800px;
    height: 1200px;
    overflow: hidden;
    background:
      radial-gradient(ellipse 80% 45% at 50% 38%, var(--glow-violet) 0%, var(--deep-blue) 45%, var(--night) 85%);
  }
  .cover-photo {
    position: absolute;
    left: 37px;
    top: 204px;
    width: 736px;
    height: 416px;
    border-radius: 6px;
    background:
      radial-gradient(ellipse 22% 30% at 18% 28%, rgba(184,210,74,0.85) 0%, rgba(184,210,74,0) 100%),
      radial-gradient(ellipse 14% 22% at 16% 82%, rgba(184,210,74,0.7) 0%, rgba(184,210,74,0) 100%),
      radial-gradient(ellipse 16% 30% at 82% 58%, rgba(192,74,138,0.55) 0%, rgba(192,74,138,0) 100%),
      radial-gradient(ellipse 40% 55% at 50% 100%, rgba(8,12,34,0.75) 0%, rgba(8,12,34,0) 100%),
      linear-gradient(135deg, var(--screen-teal) 0%, var(--screen-cyan) 40%, #5fd0e6 60%, var(--screen-teal) 100%);
    box-shadow: 0 0 60px 20px rgba(70,150,230,0.35);
    filter: blur(1.5px) saturate(1.1);
  }
  .title-art {
    position: absolute;
    left: 0;
    top: 0;
    width: 800px;
    height: 1200px;
  }
  .title-kicker {
    font-family: 'Silkscreen', monospace;
    font-weight: 700;
    fill: var(--title-white);
  }
  .title-main {
    font-family: 'Silkscreen', monospace;
    font-weight: 700;
  }
  .title-main--yellow { fill: url(#yellowFill); }
  .title-main--red { fill: url(#redFill); }
  .subtitle {
    position: absolute;
    left: 214px;
    top: 997px;
    font-family: 'PT Sans', sans-serif;
    font-size: 23px;
    color: var(--subtitle);
  }
  .subtitle strong { font-weight: 700; }
  .author {
    position: absolute;
    left: 342px;
    top: 1068px;
    font-family: 'PT Sans', sans-serif;
    font-weight: 700;
    font-size: 25px;
    color: var(--subtitle);
  }
</style>
</head>
<body>
  <main class="cover">
    <div class="cover-photo" role="img" aria-label="Photograph of a gamer seen from behind in silhouette, wearing glowing headphones, facing a bright blue game screen in a dark room"></div>

    <svg class="title-art" viewBox="0 0 800 1200" aria-label="The Nine Paths Past Screen Compulsion">
      <defs>
        <linearGradient id="yellowFill" x1="0" y1="0" x2="1" y2="1">
          <stop offset="0" stop-color="#d9df33"/>
          <stop offset="0.5" stop-color="#a7ad1c"/>
          <stop offset="1" stop-color="#d9df33"/>
        </linearGradient>
        <linearGradient id="redFill" x1="0" y1="0" x2="1" y2="1">
          <stop offset="0" stop-color="#e8182c"/>
          <stop offset="0.5" stop-color="#a80f1d"/>
          <stop offset="1" stop-color="#e8182c"/>
        </linearGradient>
      </defs>
      <text class="title-kicker" x="213" y="720" font-size="36" textLength="444" lengthAdjust="spacingAndGlyphs">THE NINE PATHS PAST</text>
      <text class="title-main title-main--yellow" x="204" y="860" font-size="165" textLength="462" lengthAdjust="spacingAndGlyphs">SCREEN</text>
      <text class="title-main title-main--red" x="202" y="975" font-size="120" textLength="466" lengthAdjust="spacingAndGlyphs">COMPULSION</text>
    </svg>

    <p class="subtitle">A <strong>Practical Route</strong> Through <strong>Console Overuse</strong></p>
    <p class="author">by Orrin Falkett</p>
  </main>
</body>
</html>
```